Website for New Phone Company

Our company "Lagoonway Telecom" requires a new web-site.

We enable Pacific Islanders (Fijians, Samoans, Tongans) to speak to their friends and family back home for a fraction of the cost of other phone companies whilst maintaining a quality. Our target audience is price sensitive but is demanding with quality, we would like them to gather a feel that they are dealing with a safe company that is orientated towards the Pacific Island community, has low pricing and yet doesn't compromise on quality.

We are going to be marketing via online channels and so a Google friendly web-site is important. We essentially need three pages designed which we will use with our content.

Page 1 - Homepage Lagoonway Telecom - Our prime brand is Lagoonway Telecom and we would like to promote this brand on our web-site.

However, we have three plans under this brand called Verelo, Makiri and Nemali. We would like the main page to have three unique service offerings for Nemali, Makiri and Verelo. Something along the lines of being able to choose a plan down on the page. I would like to give examples here of companies in our industry that are extremely successful in this trade i.e. www.dialquay.co.nz, www.9speak.co.nz, www.telvira.com

The objective of this design is to present the customer with three unique offerings targeted to Samoa (Nemali), Makiri (Tonga) and Verelo (Fiji).

Page 2 - Content/Template Page for Lagoonway Telecom - We require a page where we can place content like About Us, Contact Us etc.

Page 3 - We require a single design that will fit all three brands as per the brand images attached for Verelo, Nemali and Makiri. This will almost be used as a landing page to brand the plan exclusively under our company. All three plans / service offerings are being marketed under "Lagoonway Telecom" which makes it important to use both the service offering logo as well as the company logo. This page needs to act more as a promotional page where it promotes our service offering. e.g. Call Samoa from only 50c a minute type of thing.

The objective of the design of the landing / service offering page is to entice the customer to act upon the offer by joining our organisation.

We will be available throughout the process to guide you better.
Updates

Project Deadline Extended
Reason: We haven't received suitable designs to choose from. We would like to see quality work not quantity.

Industry/Entity Type

It Company

```html
<!DOCTYPE html>
<html lang="en">
<head>
<meta charset="utf-8">
<title>Lagoonway Telecom</title>
<link href="https://fonts.googleapis.com/css2?family=Arvo:wght@400;700&family=Hind:wght@300;400;500&display=swap" rel="stylesheet">
<style>
:root{
  --slate:#434a52;
  --slate-line:#545b63;
  --red:#d9261c;
  --ink:#333;
  --muted:#9a9a9a;
  --hairline:#e4e4e4;
  --blush:#f3ebeb;
  --band:#f4f2f2;
  --white:#fff;
}
*{box-sizing:border-box;margin:0;padding:0}
html,body{width:883px;height:1200px;overflow:hidden;background:var(--white)}
body{position:relative;font-family:"Hind",sans-serif;color:var(--ink)}
.abs{position:absolute}

.main-nav{left:0;top:14px;width:883px;height:82px;background:var(--slate);display:flex;justify-content:center;padding-left:10px}
.main-nav a{font-family:"Arvo",serif;font-weight:700;color:var(--white);text-decoration:none;font-size:17px;letter-spacing:.5px;display:flex;align-items:center;padding:0 24px;border-left:2px solid var(--slate-line)}
.main-nav a:first-child{border-left:none}

.brand{left:104px;top:128px}
.brand .dot{display:block;width:38px;height:38px;border-radius:50%;background:var(--red);margin:0 0 6px 34px}
.brand .name{font-size:18px;line-height:18px;font-weight:400;color:#555;display:block}

.util-links{left:296px;top:116px;display:flex;gap:9px;font-size:7.5px;color:#999;text-transform:uppercase;letter-spacing:.2px}
.util-links .sel{color:var(--red);margin-left:4px}

.search{left:440px;top:164px;width:181px;height:33px;border:1px solid #ccc;font-size:11px;color:#aaa;padding:9px 7px}
.search svg{position:absolute;right:16px;top:10px}
.cart{left:639px;top:165px;width:146px;height:32px;background:var(--red);color:var(--white);font-size:11px;font-weight:500;display:flex;align-items:center;justify-content:center;gap:8px}

.hero-bg{left:0;top:223px;width:883px;height:358px;background:var(--blush)}
.hero-photo{left:368px;top:223px;width:515px;height:358px;background:linear-gradient(100deg,var(--blush) 0%,#d9cfc9 22%,#b8b5b0 55%,#9a9c9c 100%)}
.hero-title{left:110px;top:307px;font-size:18.5px;line-height:20px;font-weight:500;color:var(--red);text-transform:uppercase}
.hero-copy{left:110px;top:371px;width:270px;font-size:10.5px;line-height:22px;color:#bbb;text-transform:uppercase}
.price{left:110px;top:426px;font-size:10.5px;color:#bbb;text-transform:uppercase}
.price b{color:var(--red);font-weight:500}
.price small{color:var(--red);font-size:7px}
.btn{background:var(--red);color:var(--white);font-size:11px;display:flex;align-items:center;justify-content:center;text-decoration:none}
.hero-btn{left:116px;top:484px;width:95px;height:39px;font-weight:500;text-transform:uppercase}

.plans{left:61px;top:609px;width:721px;height:206px;border:2px solid #eee;display:flex}
.plan{flex:1;border-left:2px solid #eee;position:relative}
.plan:first-child{border-left:none}
.plan-name{position:absolute;top:40px;left:0;right:0;display:flex;justify-content:center;align-items:center;gap:6px;font-size:18px;color:var(--slate)}
.plan-name i{width:12px;height:12px;border-radius:50%;background:var(--red);display:block}
.plan p{position:absolute;top:86px;left:48px;width:150px;font-size:10.5px;line-height:18px;color:#999}
.plan .btn{position:absolute;left:76px;top:168px;width:87px;height:25px}

.info{left:0;top:872px;width:883px;height:258px;background:var(--band)}
.col{top:886px;width:180px}
.col h2{font-size:24px;font-weight:400;color:#222;margin-bottom:17px;white-space:nowrap}
.col p{font-size:10.5px;line-height:18px;color:#999;text-align:justify;text-align-last:left;margin-left:2px}
.col-what{left:119px}
.col-why{left:350px}
.col-why p{margin-left:2px}
.col-how{left:592px}
.col-btn{top:1074px;width:87px;height:25px}

.footer{left:0;top:1130px;width:883px;height:70px;background:var(--slate);color:var(--white);font-size:12px}
.footer span{position:absolute;left:101px;top:28px}
</style>
</head>
<body>

<nav class="abs main-nav">
  <a href="#">HOME</a><a href="#">PRODUCT</a><a href="#">SUPPORT</a><a href="#">CONACT</a><a href="#">SHOP</a>
</nav>

<div class="abs brand">
  <span class="dot"></span>
  <span class="name">Lagoonway</span>
  <span class="name">Telecom</span>
</div>

<div class="abs util-links">
  <span>Home</span><span>Wish list (0)</span><span>My account</span><span>Shopping</span><span>Cart</span><span>Checkout</span><span>Login</span><span>Create an account</span>
  <span>$ <span class="sel">&#9660;</span></span><span>En <span class="sel">&#9660;</span></span>
</div>

<div class="abs search">Search
  <svg width="11" height="11" viewBox="0 0 11 11"><circle cx="4.5" cy="4.5" r="3.3" fill="none" stroke="#d9261c" stroke-width="1.6"/><line x1="7" y1="7" x2="10" y2="10" stroke="#d9261c" stroke-width="1.8"/></svg>
</div>
<div class="abs cart">
  <svg width="14" height="12" viewBox="0 0 14 12"><path d="M0 1h2.5l2 7h7l2-5H4" fill="none" stroke="#fff" stroke-width="1.6"/><circle cx="5.5" cy="10.5" r="1.2" fill="#fff"/><circle cx="10.5" cy="10.5" r="1.2" fill="#fff"/></svg>
  Cart : 0 Item(s) -$0.0
</div>

<div class="abs hero-bg"></div>
<div class="abs hero-photo" role="img" aria-label="Close-up photo of a finger pressing the Send key on a phone keypad"></div>
<h1 class="abs hero-title">Call your loved ones in<br>almost no cost</h1>
<p class="abs hero-copy">We offer lowest call charges for Samoa (Nemali), Makiri (Tonga) and Verelo (Fiji).</p>
<p class="abs price">Starting from :<b>$9.99</b> <small>MONTH</small></p>
<a class="abs btn hero-btn" href="#">Read More</a>

<section class="abs plans">
  <div class="plan">
    <div class="plan-name"><i></i>Nemali</div>
    <p>Lorem ipsum dolor sit amet, consectetur adipiscing elit. Aliquam tristique lectus et f ermentum iaculis.</p>
    <a class="btn" href="#">Read More</a>
  </div>
  <div class="plan">
    <div class="plan-name"><i></i>Verelo</div>
    <p>Lorem ipsum dolor sit amet, consectetur adipiscing elit. Aliquam tristique lectus et f ermentum iaculis.</p>
    <a class="btn" href="#">Read More</a>
  </div>
  <div class="plan">
    <div class="plan-name"><i></i>Makiri</div>
    <p>Lorem ipsum dolor sit amet, consectetur adipiscing elit. Aliquam tristique lectus et f ermentum iaculis.</p>
    <a class="btn" href="#">Read More</a>
  </div>
</section>

<div class="abs info"></div>
<div class="abs col col-what">
  <h2>What We Do</h2>
  <p>Mauris fermentum dictum magneuam leo. Ut telloribus eget elementum vel curleifend elit. Aean auctorisi et urnaliqt. Duirpis. Inteerutrm ante eu lastib ulumiamur ulla fn nec eros. Nam ullamcorper dictum nunc.</p>
</div>
<div class="abs col col-why">
  <h2 style="margin-left:18px">Why Choose Us</h2>
  <p>Mauris fermentum dictum magneuam leo. Ut telloribus eget elementum vel curleifend elit. Aean auctorisi et urnaliqt. Duirpis. Inteerutrm ante eu lastib ulumiamur ulla fn nec eros. Nam ullamcorper</p>
</div>
<div class="abs col col-how">
  <h2 style="margin-left:17px">How It Work</h2>
  <p>Mauris fermentum dictum magneuam leo. Ut telloribus eget elementum vel curleifend elit. Aean auctorisi et urnaliqt. Duirpis. Inteerutrm ante eu lastib ulumiamur ulla fn nec eros. Nam ullamcorper</p>
</div>
<a class="abs btn col-btn" style="left:141px" href="#">Read More</a>
<a class="abs btn col-btn" style="left:381px" href="#">Read More</a>
<a class="abs btn col-btn" style="left:621px" href="#">Read More</a>

<footer class="abs footer"><span>&copy; 2014. All Right Reserved</span></footer>

</body>
</html>
```